Real Estate Agent who sells beach front condos needs a template for a monthly postcard campaign.

Marcy Tillford, Homebroker with Quenlow Real Estate and Development, Licensed in Florida and Alabama, 251-374-5820, marcytillford.realtor, marcyktillford@mailbox-example.com. Need a postcard template which will allow me to type in recipe instructions and insert a photo of the finished food product. The recipe and photo will change every month, so I need this to be something I can easily change and reorder every month. I sell beach condos primarily. I'd like large photos of the food. Glossy card on both sides.

Target Market(s)

buyers and sellers of homes, condos, lots

Industry/Entity Type

Real Estate Agent

Requirements
Must have
• my contact information, my photo, my company name (Quenlow Real Estate and Development), the Equal Dwelling Logo, the Homebroker Logo, the statement "Contact me for all your Real Estate needs!", a template on the front side that will let me change the photograph at will, and a template on the back side that will let me type words.
Nice to have
• For my contact info and photo to stand out also.

```html
<!DOCTYPE html>
<html lang="en">
<head>
<meta charset="utf-8">
<title>Marcy Tillford – Recipe Postcard</title>
<link href="https://fonts.googleapis.com/css2?family=Courgette&family=Kaushan+Script&family=Roboto+Condensed:wght@400;700&family=Open+Sans:wght@400;700&family=Cormorant+SC:wght@500&display=swap" rel="stylesheet">
<style>
:root{
  --stage:#3b2418;
  --lime:#8cba2a;
  --lime-dark:#6d9a1c;
  --mint:#7fd36e;
  --mint-light:#9fe08d;
  --wood:#d9a55a;
  --wood-dark:#b97f36;
  --maroon:#8a2a1c;
  --ink:#2a1e14;
  --white:#ffffff;
  --line:#4a90e2;
}
*{margin:0;padding:0;box-sizing:border-box}
html,body{width:1200px;height:488px;overflow:hidden}
body{background:var(--stage);position:relative;font-family:"Open Sans",sans-serif}
.card{position:absolute;top:45px;width:538px;height:383px;overflow:hidden}
.card--front{left:50px;background:var(--lime)}
.card--back{left:625px;background:var(--white)}

/* front */
.recipe-title{position:absolute;left:0;top:0;width:326px;height:85px;background:var(--lime);padding:14px 10px 0 16px;
  font-family:"Courgette",cursive;color:var(--maroon);font-size:21px;line-height:29px;font-weight:400}
.food-photo{position:absolute;left:0;top:85px;width:326px;height:188px;
  background:radial-gradient(ellipse at 45% 55%,#e8c77a 0%,#d7a95a 35%,#c9875a 60%,#e9e4dc 85%)}
.recipe-panel{position:absolute;left:326px;top:0;width:212px;height:273px;
  background:linear-gradient(100deg,var(--wood) 0%,#e3b36b 45%,var(--wood-dark) 100%);
  border-left:3px solid var(--maroon);padding:14px 8px 0 6px;
  font-family:"Roboto Condensed",sans-serif;color:var(--ink);font-size:8.6px;line-height:11px}
.recipe-panel h3{font-size:10px;font-weight:700;margin-bottom:3px}
.recipe-panel ul{list-style:none;margin-bottom:9px}
.recipe-panel p{margin-bottom:9px}
.gift-band{position:absolute;left:0;top:273px;width:538px;height:110px;background:var(--lime-dark)}
.gift-photo{position:absolute;left:24px;top:10px;width:72px;height:86px;border:3px solid var(--lime);border-radius:8px;
  background:linear-gradient(180deg,#e9cf95,#c99a5c 60%,#3a3a3a)}
.gift-text{position:absolute;left:107px;top:17px;width:215px;color:var(--ink);font-size:11px;line-height:14px;white-space:nowrap}
.gift-text strong{font-size:14px;display:block;color:var(--white);font-weight:700;margin-bottom:1px}
.gift-text .tag{color:var(--white)}
.quote{position:absolute;left:334px;top:30px;width:190px;text-align:center;color:var(--white);
  font-family:"Cormorant SC",serif;font-size:11.5px;line-height:14px}

/* back */
.promo-panel{position:absolute;left:0;top:0;width:277px;height:383px;
  background:linear-gradient(160deg,var(--mint-light),var(--mint) 50%,#6fca60);color:var(--white)}
.agent-photo{position:absolute;left:80px;top:23px;width:117px;height:132px;border:4px solid #e8f5e2;
  background:linear-gradient(180deg,#edd79f,#cda064 55%,#3c3c3c)}
.agent-name{position:absolute;left:52px;top:160px;font-family:"Kaushan Script",cursive;font-size:28px;line-height:30px;white-space:nowrap}
.agent-role{position:absolute;left:52px;top:190px;font-family:"Kaushan Script",cursive;font-size:14px;white-space:nowrap}
.license{position:absolute;left:62px;top:217px;font-size:10px;opacity:.9}
.company{position:absolute;left:50px;top:249px;color:var(--ink);font-weight:700;font-size:11px;line-height:14px;white-space:nowrap}
.cta{position:absolute;left:50px;top:281px;font-family:"Kaushan Script",cursive;font-size:16px;line-height:22px}
.contact{position:absolute;left:75px;top:330px;width:200px;color:var(--ink);font-size:9.5px;line-height:12px;white-space:nowrap}
.contact .phone{font-size:13px;font-weight:700;line-height:15px}
.return-label{position:absolute;left:315px;top:17px;width:117px;height:40px;background:var(--mint);color:var(--white);padding:3px 5px;white-space:nowrap;overflow:hidden}
.return-label .n{font-family:"Kaushan Script",cursive;font-size:14px;line-height:14px}
.return-label .r{font-family:"Kaushan Script",cursive;font-size:9px;line-height:10px}
.return-label .l{font-size:7px}
.stamp{position:absolute;left:452px;top:17px;width:61px;height:62px;border:1.5px solid var(--line)}
.address-line{position:absolute;left:317px;width:198px;border-top:1.5px solid var(--line)}
.brand-marks{position:absolute;left:318px;top:336px;width:210px;display:flex;justify-content:space-between;align-items:center;
  font-size:8px;font-weight:700;color:var(--maroon);white-space:nowrap}
.brand-marks span{display:flex;align-items:center;gap:3px}
.brand-marks i{display:inline-block;width:8px;height:8px;background:var(--ink)}
.brand-marks .plain{color:var(--ink)}
</style>
</head>
<body>
<section class="card card--front">
  <h1 class="recipe-title">Linguine with Shrimp, Garlic, Baby Spinach, and Tomatoes</h1>
  <div class="food-photo" role="img" aria-label="Photo of linguine with shrimp, spinach and tomatoes"></div>
  <div class="recipe-panel">
    <h3>Ingredients:</h3>
    <ul>
      <li>1 lb linguine</li>
      <li>3 tbsp extra virgin olive oil</li>
      <li>1 pound shrimp</li>
      <li>1 tsp Harborline seasoning</li>
      <li>1/4 tsp crushed red pepper flakes</li>
      <li>3 cloves minced garlic</li>
      <li>2 big handfuls of baby spinach leaves</li>
      <li>3 on-the-vine ripe or heirloom tomatoes, diced</li>
      <li>parmigiano reggiano for grating on top</li>
    </ul>
    <h3>Directions:</h3>
    <p>Cook the linguine according to the directions listed above. Drain the pasta, and immediately toss it with the 3 tbsp extra virgin olive oil, baby spinach, and tomatoes. The residual heat from the pasta will cook the tomatoes and spinach ever so slightly and take the raw edge off.</p>
    <p>Saute the shrimp with the garlic, Harborline, red pepper flakes, and toss it with your pasta. Grate some parmigiano on top. Enjoy.</p>
  </div>
  <div class="gift-band">
    <div class="gift-photo" role="img" aria-label="Headshot of Marcy Tillford"></div>
    <div class="gift-text">
      <strong>A gift from Marcy Tillford</strong>
      <span class="tag">Your Recipe for Success In Real Estate</span><br>
      &#9990; 251.374.5820<br>
      E: marcyktillford@mailbox-example.com
    </div>
    <p class="quote">“The most treasured things passed down from generation to generation are the Family recipes.” ~ Everett Lang</p>
  </div>
</section>

<section class="card card--back">
  <div class="promo-panel">
    <div class="agent-photo" role="img" aria-label="Portrait of Marcy Tillford"></div>
    <div class="agent-name">Marcy Tillford</div>
    <div class="agent-role">Your Gulf Coast Homebroker</div>
    <div class="license">Licensed in Alabama &amp; Florida</div>
    <div class="company">Homebroker with<br>Quenlow Real Estate &amp; Development</div>
    <div class="cta">Contact me for all your<br>Real Estate needs!</div>
    <div class="contact">
      <span class="phone">&#9990; 251.374.5820</span><br>
      E: marcyktillford@mailbox-example.com<br>
      marcytillford.realtor
    </div>
  </div>
  <div class="return-label">
    <div class="n">Marcy Tillford</div>
    <div class="r">Your Gulf Coast Homebroker</div>
    <div class="l">Licensed in Alabama &amp; Florida</div>
  </div>
  <div class="stamp"></div>
  <div class="address-line" style="top:164px"></div>
  <div class="address-line" style="top:189px"></div>
  <div class="address-line" style="top:214px"></div>
  <div class="address-line" style="top:239px"></div>
  <div class="brand-marks">
    <span>QUENLOW</span>
    <span class="plain"><i></i>Equal Dwelling</span>
    <span class="plain"><i></i>Homebroker</span>
  </div>
</section>
</body>
</html>
```